NEW Website DESIGN for Brightwell Panes & Stoneworks Company

Brand New website, contemporary, clean, visual (images), not busy. ATTACHED IS OUR LOG THAT YOU MUST USE.

The company is called Brightwell Panes & Stoneworks (BrightwellPS)
www.brightwellps.com
The website should be www.brightwellpns.com
one page for glass one page for solid surfaces www.brightwellpanesplashes.co.uk
www.brightwellstoneworkss.co.uk

Target Market(s)

Hotels, Commercial projects, Small focus on residential

Industry/Entity Type

Construction

Number of Pages Required

5+ page

Font styles to use
Sans Serif

Requirements
Must have
• COLOURS AS PER OUR LOGO - WHITE/YELLOW/GREY - WHITE BACK GROUND
• CLEAR SIMPLE NAVIGATION - MODER CLEAN CUT - DESIGN FEEL
• LATEST NAVIGATION FOR IMAGES and text to include per project details
• WORK/PROJECT AREA - NEWS AREA - TEAM AREA/ABOUT US/CONTACT US
• NEW PAGEwww.brightwellpanesplashes.co.uk - NEW PAGE www.brightwellstoneworkss.co.uk
• PLEASE COPY THIS TYPE OF TEMPALTE
• https://www.harlowmead.co.uk/project/grand-halls/
• MOBILE READY
• WORDPRESS
• MODERN IMAGES INCLUDING VELMARA KESTRIN AND GLASS PROJECTS
Nice to have
• NEW DESIGN MODER FRESH
• WEBSITES I LIKE THE TEMPLATE SHOULD BE LIKE THE WEBSITE BELOW
• https://www.harlowmead.co.uk/
Should not have
• NOT Old fashion template, not busy NAVIGATION
• NO BLACK
• NO DARK GREYS
• NOT LOTS OF YELLOW
• RESDENTIAL IMAGES

```html
<!DOCTYPE html>
<html lang="en">
<head>
<meta charset="utf-8">
<title>Brightwell Panes &amp; Stoneworks</title>
<link rel="stylesheet" href="https://fonts.googleapis.com/css2?family=Montserrat:wght@500;600&family=Lato:ital,wght@0,400;0,700;1,400&display=swap">
<style>
:root{
  --yellow:#fbea22;
  --white:#ffffff;
  --ink:#1e1e1e;
  --text:#333333;
  --grey-soft:#e9eaea;
  --card-dark:rgba(38,38,38,.93);
  --footer:#1a1a1a;
  --contact-dark:rgba(40,40,40,.9);
}
*{box-sizing:border-box;margin:0;padding:0}
html,body{width:1200px;height:3586px;overflow:hidden;background:var(--white)}
body{position:relative;font-family:"Lato",sans-serif;color:var(--text)}
.section{position:absolute;left:0;width:1200px;overflow:hidden}
.photo{position:absolute;inset:0}
.heading{position:absolute;left:0;width:100%;text-align:center;font-family:"Montserrat",sans-serif;font-weight:500;font-size:36px;letter-spacing:1px;color:var(--ink)}
.btn{position:absolute;display:flex;align-items:center;justify-content:center;background:var(--yellow);border:2px solid var(--ink);font-family:"Montserrat",sans-serif;font-weight:500;font-size:18px;color:var(--ink)}

/* hero */
.hero{top:0;height:677px}
.hero .photo{background:linear-gradient(180deg,#8e928f 0%,#c9cbc6 40%,#a9aba6 70%,#7b7d79 100%)}
.brand-badge{position:absolute;left:447px;top:177px;width:296px;height:296px;border-radius:50%;background:var(--white);border:14px solid var(--yellow);display:flex;align-items:center;justify-content:center;text-align:center}
.brand-name{font-family:"Montserrat",sans-serif;font-weight:600;font-size:22px;line-height:1.3;color:#4a4a4a;width:200px}
.menu-toggle{position:absolute;left:684px;top:196px;width:54px;height:54px;background:var(--ink);border-radius:6px;display:flex;flex-direction:column;justify-content:center;align-items:center;gap:6px}
.menu-toggle span{display:block;width:26px;height:4px;background:var(--yellow)}
.slider-dots{position:absolute;top:583px;left:0;width:100%;display:flex;justify-content:center;gap:12px}
.slider-dots span{width:20px;height:20px;border-radius:50%;border:2px solid var(--white);background:transparent}
.slider-dots span.active{background:var(--white)}

/* about */
.about{top:710px;height:414px}
.about .photo{background:linear-gradient(90deg,#c4cdd0 0%,#eef0ef 25%,#f6f6f5 60%,#e2e3e1 85%,#b9bcba 100%)}
.about .heading{top:62px}
.about-text{position:absolute;left:258px;top:125px;width:684px;text-align:center;font-size:14.5px;line-height:31px;color:#444}
.about .btn{left:516px;top:282px;width:170px;height:60px}

/* work */
.work{top:1159px;height:921px}
.work .photo{background:linear-gradient(180deg,#f3f3f2 0%,#ececea 60%,#dddbd6 100%)}
.work .heading{top:57px}
.project-card{position:absolute;width:322px;height:320px;border:4px solid var(--white);box-shadow:0 0 0 1px #bdbdbd}
.project-card .thumb{position:absolute;inset:0}
.project-card .caption{position:absolute;left:10px;width:290px;background:rgba(255,255,255,.93);padding:14px 14px 12px}
.caption h3{font-family:"Lato",sans-serif;font-weight:400;font-size:18px;color:var(--ink);margin-bottom:10px}
.caption p{font-style:italic;font-size:14.5px;line-height:27px;color:#8a8a8a}
.cap-bottom{bottom:24px}
.cap-top{top:18px}

/* news */
.news{top:2116px;height:686px}
.news .photo{background:linear-gradient(180deg,#9fb09a 0%,#cfd6cc 45%,#e8e6e1 70%,#d3cfc8 100%)}
.news .heading{top:60px}
.news-card{position:absolute;top:150px;width:500px;height:364px;background:var(--card-dark);color:var(--white);padding:38px 34px}
.news-date{font-style:italic;font-size:19px;margin-bottom:34px}
.news-title{font-style:italic;font-size:20px;line-height:31px;margin-bottom:16px}
.news-body{font-size:13px;line-height:25px;color:#e6e6e6}
.news .btn{left:507px;top:573px;width:186px;height:60px}

/* contact */
.contact{top:2835px;height:667px}
.contact .photo{background:linear-gradient(135deg,#cbbfa9 0%,#ecebe6 45%,#f4f2ee 70%,#c9c2b4 100%)}
.contact-panel{position:absolute;left:0;top:0;width:600px;height:667px;background:var(--contact-dark);color:var(--white);padding-left:79px}
.contact-title{position:absolute;top:63px;font-family:"Montserrat",sans-serif;font-weight:600;font-size:34px}
.contact-address{position:absolute;top:132px;font-style:italic;font-size:15px}
.contact-tel{position:absolute;top:172px;font-family:"Montserrat",sans-serif;font-weight:600;font-size:19px}
.field{position:absolute;left:79px;width:466px;border:2px solid #d9d9d9;padding:14px 18px;font-size:15px;color:var(--white)}
.field-name{top:220px;height:60px}
.field-email{top:303px;height:60px}
.field-message{top:387px;height:120px}
.send-btn{position:absolute;left:79px;top:535px;width:153px;height:60px;background:var(--white);color:var(--ink);display:flex;align-items:center;justify-content:center;font-family:"Montserrat",sans-serif;font-weight:500;font-size:17px}

/* footer */
.site-footer{position:absolute;top:3502px;left:0;width:1200px;height:84px;background:var(--footer);color:var(--white)}
.copyright{position:absolute;left:79px;top:33px;font-size:13.5px}
.copyright strong{font-weight:700}
.social-links{position:absolute;left:924px;top:22px;display:flex;gap:12px}
.social-links span{width:42px;height:42px;border:1.5px solid #cfcfcf}
</style>
</head>
<body>

<header class="section hero">
  <div class="photo" role="img" aria-label="Bright modern living room with white sofa, glass table and tall windows"></div>
  <div class="brand-badge"><div class="brand-name">Brightwell Panes &amp; Stoneworks</div></div>
  <div class="menu-toggle" aria-label="Menu"><span></span><span></span><span></span></div>
  <div class="slider-dots"><span></span><span class="active"></span><span></span><span></span></div>
</header>

<section class="section about">
  <div class="photo" role="img" aria-label="Airy interior with large glass windows overlooking hills"></div>
  <h2 class="heading">ABOUT US</h2>
  <p class="about-text">Lorem Ipsum is simply dummy text of the printing and typesetting industry. Lorem Ipsum has been the industry's standard dummy text ever since the 1500s, when an unknown printer took a galley of type and scrambled it to make a type specimen book. It has survived not only five centuries, but also the leap into electronic typesetting, remaining essentially unchanged.</p>
  <div class="btn">READ MORE</div>
</section>

<section class="section work">
  <div class="photo" role="img" aria-label="Soft bright interior backdrop"></div>
  <h2 class="heading">OUR WORK</h2>

  <article class="project-card" style="left:76px;top:161px">
    <div class="thumb" role="img" aria-label="White kitchen with solid surface worktops" style="background:linear-gradient(160deg,#e9e6de,#b9a57a 60%,#6f6a5c)"></div>
    <div class="caption cap-bottom"><h3>Lorem typesetting industry.</h3><p>Lorem Ipsum is simply dummy text printing and typesetting industry.</p></div>
  </article>
  <article class="project-card" style="left:440px;top:161px">
    <div class="thumb" role="img" aria-label="Glass balcony doors opening onto a terrace" style="background:linear-gradient(180deg,#c9d6c4,#8fa694 55%,#dfe1dc)"></div>
    <div class="caption cap-top"><h3>Lorem typesetting industry.</h3><p>Lorem Ipsum is simply dummy text printing and typesetting industry.</p></div>
  </article>
  <article class="project-card" style="left:798px;top:161px">
    <div class="thumb" role="img" aria-label="Bathroom with glass shower enclosure and brick wall" style="background:linear-gradient(160deg,#5b3b2c,#a7836a 50%,#d9d3cb)"></div>
    <div class="caption cap-bottom"><h3>Lorem typesetting industry.</h3><p>Lorem Ipsum is simply dummy text printing and typesetting industry.</p></div>
  </article>

  <article class="project-card" style="left:76px;top:514px">
    <div class="thumb" role="img" aria-label="Bathroom with twin framed mirrors and vanity" style="background:linear-gradient(160deg,#eceae5,#b98a55 50%,#d7d2c8)"></div>
    <div class="caption cap-bottom"><h3>Lorem typesetting industry.</h3><p>Lorem Ipsum is simply dummy text printing and typesetting industry.</p></div>
  </article>
  <article class="project-card" style="left:440px;top:514px">
    <div class="thumb" role="img" aria-label="Lounge with glass wall and armchair" style="background:linear-gradient(180deg,#e6e8e6,#c7c3b8 55%,#a68f70)"></div>
    <div class="caption cap-top"><h3>Lorem typesetting industry.</h3><p>Lorem Ipsum is simply dummy text printing and typesetting industry.</p></div>
  </article>
  <article class="project-card" style="left:798px;top:514px">
    <div class="thumb" role="img" aria-label="Hotel bedroom with large windows" style="background:linear-gradient(160deg,#9a9a7c,#d8d2c1 50%,#f0ede6)"></div>
    <div class="caption cap-bottom"><h3>Lorem typesetting industry.</h3><p>Lorem Ipsum is simply dummy text printing and typesetting industry.</p></div>
  </article>
</section>

<section class="section news">
  <div class="photo" role="img" aria-label="Sunlit room with floor-to-ceiling windows and garden view"></div>
  <h2 class="heading">LATEST NEWS</h2>
  <article class="news-card" style="left:76px">
    <p class="news-date">08 August 2018</p>
    <h3 class="news-title">Lorem Ipsum is simply dummy text of the printing and typesetting industry.</h3>
    <p class="news-body">Lorem Ipsum is simply dummy text of the printing and typesetting industry. Lorem Ipsum has been the industry's standard dummy text ever since the 1500s, when an unknown printer took a galley of type and scrambled it to make a type specimen book. It has survived not only five centuries, but also the leap into electronic typesetting, remaining essentially unchanged.</p>
  </article>
  <article class="news-card" style="left:624px">
    <p class="news-date">08 August 2018</p>
    <h3 class="news-title">Lorem Ipsum is simply dummy text of the printing and typesetting industry.</h3>
    <p class="news-body">Lorem Ipsum is simply dummy text of the printing and typesetting industry. Lorem Ipsum has been the industry's standard dummy text ever since the 1500s, when an unknown printer took a galley of type and scrambled it to make a type specimen book. It has survived not only five centuries, but also the leap into electronic typesetting, remaining essentially unchanged.</p>
  </article>
  <div class="btn">VIEW ALL POSTS</div>
</section>

<section class="section contact">
  <div class="photo" role="img" aria-label="Double-height living space with glass balustrade and white sofa"></div>
  <div class="contact-panel">
    <h2 class="contact-title">CONTACT US</h2>
    <p class="contact-address">14 Marlow Quay Ste 210 Harbourton IL 60611-0482</p>
    <p class="contact-tel">TEL : 555-014-2290</p>
  </div>
  <div class="field field-name">Name :</div>
  <div class="field field-email">E - Mail :</div>
  <div class="field field-message">Message :</div>
  <div class="send-btn">SEND</div>
</section>

<footer class="site-footer">
  <p class="copyright">Copyright © <strong>BRIGHTWELL PANES &amp; STONEWORKS</strong> - All Right Reserved</p>
  <div class="social-links" aria-label="Social links"><span></span><span></span><span></span><span></span></div>
</footer>

</body>
</html>
```